I need a design to display a result on a range line

For example - If I have a blood sugar result and I want to display it on a line so that I can display it in picture terms so that it can be understood more.
I want to input the result in a calculator so it can be displayed on the range line.

I want it so I can customise it and apply it to other results my self too.

```html
<!DOCTYPE html>
<html lang="en">
<head>
<meta charset="UTF-8">
<title>Blood Sugar Range Line</title>
<link href="https://fonts.googleapis.com/css2?family=Lato:wght@700&display=swap" rel="stylesheet">
<style>
  :root {
    --canvas-bg: #ffffff;
    --text: #111111;
    --track: #7a7a7a;
    --low: #0a7cff;
    --optimal: #00c853;
    --prediabetic: #ffc00a;
    --high: #9b0007;
    --optimal-tint: #eaf7f0;
    --high-tint: #f7eaea;
  }
  html, body {
    margin: 0;
    padding: 0;
    overflow: hidden;
    background: var(--canvas-bg);
  }
  .range-canvas {
    position: relative;
    width: 1200px;
    height: 675px;
    background: var(--canvas-bg);
    font-family: "Lato", sans-serif;
    font-weight: 700;
    color: var(--text);
    overflow: hidden;
  }
  .zone-highlight {
    position: absolute;
    top: 252px;
    width: 176px;
    height: 199px;
    border-radius: 21px;
  }
  .zone-highlight--optimal { left: 392px; background: var(--optimal-tint); }
  .zone-highlight--high { left: 780px; background: var(--high-tint); }
  .range-track {
    position: absolute;
    left: 0;
    top: 0;
  }
  .range-stop {
    position: absolute;
    width: 180px;
    margin-left: -90px;
    text-align: center;
    font-size: 19px;
    line-height: 1;
  }
  .range-stop__value { top: 280px; }
  .range-stop__label { top: 411px; }
  .stop-low { left: 283px; }
  .stop-optimal { left: 480px; }
  .stop-prediabetic { left: 677px; }
  .stop-high { left: 873px; }
</style>
</head>
<body>
  <main class="range-canvas">
    <div class="zone-highlight zone-highlight--optimal"></div>
    <div class="zone-highlight zone-highlight--high"></div>

    <svg class="range-track" width="1200" height="675" viewBox="0 0 1200 675" aria-hidden="true">
      <line x1="283" y1="352" x2="873" y2="352" stroke="var(--track)" stroke-width="1.6"/>
      <circle cx="283" cy="352" r="34.5" fill="var(--low)"/>
      <circle cx="480" cy="352" r="34.5" fill="var(--optimal)"/>
      <circle cx="677" cy="352" r="34.5" fill="var(--prediabetic)"/>
      <circle cx="873" cy="352" r="34.5" fill="var(--high)"/>
    </svg>

    <div class="range-stop range-stop__value stop-low">&lt;4.0</div>
    <div class="range-stop range-stop__value stop-optimal">4.0-5.59</div>
    <div class="range-stop range-stop__value stop-prediabetic">5.6-6.99</div>
    <div class="range-stop range-stop__value stop-high">&ge;7.0</div>

    <div class="range-stop range-stop__label stop-low">Low</div>
    <div class="range-stop range-stop__label stop-optimal" style="top:413px">Optimal</div>
    <div class="range-stop range-stop__label stop-prediabetic">Pre-Diabetic</div>
    <div class="range-stop range-stop__label stop-high">High</div>
  </main>
</body>
</html>
```